Brit Rock covers band "The Tin Kettles" requires poster for Marlowe Lounge Friday March 31st

I want a design for a poster (A3 and A4) and Facebook/Instagram ads.
Primary focus is the band name logo "The Tin Kettles", style as in attached file, followed by tag "Old Skool Brit Rock".
Backdrop to be 60's psychedelic art.
Secondary focus is the venue "The Marlowe Lounge"
Supporting text to include:
- 27 Fenwick Road, Chatswood SYDNEY
- Friday 31st March 2023
- 7:00 pm until late
- Bar sales refreshments
- NO admission fee

```html
<!DOCTYPE html>
<html lang="en">
<head>
<meta charset="utf-8">
<title>The Tin Kettles – Old Skool Brit Rock at The Marlowe Lounge</title>
<link rel="stylesheet" href="https://fonts.googleapis.com/css2?family=Oswald:wght@400;600&family=Pirata+One&display=swap">
<style>
  :root {
    --ink: #000000;
    --night: #050505;
    --paper: #ffffff;
    --acid-yellow: #f4f200;
    --neon-blue: #3a7dff;
    --neon-cyan: #6fd8ff;
    --neon-violet: #8b3fd9;
    --neon-pink: #ff3fa8;
    --neon-orange: #ff8a3d;
  }
  html, body {
    margin: 0;
    padding: 0;
    width: 910px;
    height: 1200px;
    overflow: hidden;
    background: var(--night);
  }
  .poster {
    position: relative;
    width: 910px;
    height: 1200px;
    background: var(--night);
    overflow: hidden;
    font-family: "Oswald", "Arial Narrow", sans-serif;
  }
  .psychedelic-backdrop {
    position: absolute;
    left: 0;
    top: 0;
    width: 910px;
    height: 540px;
    background:
      radial-gradient(ellipse at 50% 30%, rgba(255,255,255,0.85) 0%, rgba(255,255,255,0) 35%),
      radial-gradient(ellipse at 15% 20%, var(--neon-cyan) 0%, rgba(111,216,255,0) 45%),
      radial-gradient(ellipse at 85% 15%, var(--neon-pink) 0%, rgba(255,63,168,0) 50%),
      radial-gradient(ellipse at 80% 55%, var(--neon-orange) 0%, rgba(255,138,61,0) 40%),
      radial-gradient(ellipse at 20% 60%, var(--neon-violet) 0%, rgba(139,63,217,0) 50%),
      linear-gradient(180deg, var(--neon-blue) 0%, #6a2fb8 55%, #2a0f3a 80%, var(--night) 100%);
  }
  .band-name {
    position: absolute;
    left: 0;
    width: 910px;
    top: 110px;
    margin: 0;
    text-align: center;
    color: var(--ink);
    font-family: "Oswald", "Arial Narrow", sans-serif;
    font-weight: 600;
    text-transform: uppercase;
    line-height: 1;
  }
  .band-name .line-one {
    display: block;
    font-size: 112px;
    letter-spacing: -1px;
  }
  .band-name .line-two {
    display: block;
    font-size: 168px;
    letter-spacing: -2px;
    margin-top: 4px;
  }
  .tagline,
  .venue {
    position: absolute;
    left: 0;
    width: 910px;
    margin: 0;
    text-align: center;
    color: var(--acid-yellow);
    font-family: "Pirata One", "Times New Roman", serif;
    font-weight: 400;
    line-height: 1;
  }
  .tagline {
    top: 494px;
    font-size: 84px;
  }
  .backdrop-note {
    position: absolute;
    left: 0;
    width: 910px;
    top: 612px;
    margin: 0;
    text-align: center;
    color: var(--paper);
    font-family: Arial, Helvetica, sans-serif;
    font-weight: 700;
    font-size: 31px;
  }
  .venue {
    top: 660px;
    font-size: 80px;
  }
  .event-details {
    position: absolute;
    left: 67px;
    top: 794px;
    width: 772px;
    height: 206px;
    border: 2px solid var(--acid-yellow);
    box-sizing: border-box;
    display: flex;
    flex-direction: column;
    justify-content: center;
    align-items: center;
    color: var(--paper);
    font-size: 48px;
    font-weight: 400;
    text-transform: uppercase;
    line-height: 1.32;
    letter-spacing: -0.5px;
  }
  .event-details p,
  .extras p { margin: 0; }
  .extras {
    position: absolute;
    left: 155px;
    top: 1027px;
    width: 600px;
    height: 142px;
    background: var(--acid-yellow);
    display: flex;
    flex-direction: column;
    justify-content: center;
    align-items: center;
    color: var(--ink);
    font-size: 48px;
    font-weight: 400;
    text-transform: uppercase;
    line-height: 1.3;
    letter-spacing: -0.5px;
  }
</style>
</head>
<body>
  <main class="poster">
    <div class="psychedelic-backdrop" role="img" aria-label="60s psychedelic light show with neon swirls and a cheering crowd in silhouette"></div>

    <h1 class="band-name">
      <span class="line-one">The Tin</span>
      <span class="line-two">Kettles</span>
    </h1>

    <p class="tagline">Old Skool Brit Rock</p>
    <p class="backdrop-note">Backdrop to be 60's psychedelic art.</p>
    <h2 class="venue">The Marlowe Lounge</h2>

    <section class="event-details">
      <p>27 Fenwick Road, Chatswood Sydney</p>
      <p>- Friday 31st March 2023</p>
      <p>- 7:00 pm until late</p>
    </section>

    <section class="extras">
      <p>- Bar sales refreshments</p>
      <p>- No admission fee</p>
    </section>
  </main>
</body>
</html>
```